Brackwell Immigration Law

We need a web design for our existing company www.brackwellcounsel.co.uk. We are an immigration consultancy. The final design should communicate professionalism, integrity and affordability.

Industry/Entity Type

It Company

Logo Text

Brackwell Counsel Partners

Number of Pages Required

5+ page

Font styles to use
Serif

Requirements
Must have
• I want to have the same silhouette logo but something different in positioning..
Nice to have
• Please have a look at these websites:
• https://www.travelpathguide.co.uk/visa_uk/
• http://www.oakdenadvisers.co.uk/
• http://www.myrtlegatelaw.org/index.php
• www.brackwellcounsel.co.uk

```html
<!DOCTYPE html>
<html lang="en">
<head>
<meta charset="utf-8">
<title>Brackwell Counsel Partners</title>
<link href="https://fonts.googleapis.com/css2?family=Libre+Baskerville:wght@400;700&family=Open+Sans:wght@400;600;700&display=swap" rel="stylesheet">
<style>
:root{
  --accent:#f5a300;
  --dark:#1c1c1c;
  --darker:#121212;
  --ink:#333;
  --muted:#777;
  --line:#e2e2e2;
  --paper:#ffffff;
  --soft:#f4f4f4;
}
*{box-sizing:border-box;margin:0;padding:0}
html,body{width:710px;height:1200px;overflow:hidden}
body{font-family:"Open Sans",Arial,sans-serif;color:var(--ink);background:var(--paper);font-size:8px;line-height:1.5}
.serif{font-family:"Libre Baskerville",Georgia,serif}
.wrap{width:616px;margin:0 auto;position:relative}

.topbar{height:20px;background:var(--darker);color:#ccc;font-size:8px}
.topbar .wrap{display:flex;justify-content:flex-end;align-items:center;height:20px;gap:5px}
.topbar svg{width:8px;height:8px}

.header{height:34px;background:var(--paper);border-bottom:1px solid var(--line)}
.header .wrap{display:flex;justify-content:space-between;align-items:center;height:34px}
.brand{display:flex;align-items:center;gap:6px}
.brand-mark{width:16px;height:16px;background:var(--accent)}
.brand-name{font-family:"Libre Baskerville",Georgia,serif;font-weight:700;font-size:10px;color:var(--dark)}
.nav{display:flex;gap:16px;font-size:7.5px;font-weight:600;text-transform:uppercase;color:#444}
.nav .active{color:var(--accent)}

.hero{height:251px;position:relative;background:linear-gradient(135deg,#3a3129 0%,#1a1714 55%,#2b2420 100%);color:#fff;text-align:center}
.hero-photo{position:absolute;inset:0;background:radial-gradient(ellipse at 35% 70%,rgba(150,110,70,.45),transparent 60%),radial-gradient(ellipse at 75% 40%,rgba(120,30,30,.35),transparent 55%)}
.hero-content{position:relative;padding-top:48px}
.hero-kicker{font-size:10px;letter-spacing:1px;text-transform:uppercase;color:#ddd}
.hero-title{font-size:22px;letter-spacing:1.5px;text-transform:uppercase;margin:8px 0 10px}
.hero-text{width:360px;margin:0 auto;font-size:8px;color:#ddd}
.btn{display:inline-block;background:var(--accent);color:#fff;font-weight:700;font-size:7.5px;text-transform:uppercase;padding:7px 18px;margin-top:14px}

.services{padding:18px 0 0;height:215px}
.services .wrap{display:flex;gap:14px}
.cards{display:flex;gap:12px;flex:1}
.card{width:152px;text-align:center}
.card-title{font-size:7.5px;font-weight:700;text-transform:uppercase;color:var(--dark);margin-bottom:5px}
.card-photo{height:86px;background:linear-gradient(135deg,#c9d3dc,#8d9aa6)}
.card-text{font-size:6.5px;color:var(--muted);margin:6px 4px}
.btn-outline{display:inline-block;border:1px solid #bbb;font-size:6.5px;font-weight:700;padding:3px 10px;text-transform:uppercase;color:#444}
.contact{width:140px;border:1px solid var(--line);padding:8px 10px;margin-top:-6px}
.contact h3{font-size:8px;text-transform:uppercase;text-align:center;color:var(--dark);margin-bottom:8px}
.field{border:1px solid var(--line);height:15px;font-size:6.5px;color:#999;padding:2px 5px;margin-bottom:6px}
.field.tall{height:30px}
.contact .submit{display:block;width:42px;margin-left:auto;background:var(--accent);color:#fff;font-size:6.5px;font-weight:700;text-align:center;padding:3px 0;text-transform:uppercase}

.about{height:150px;text-align:center}
.eyebrow{font-size:7px;letter-spacing:.8px;text-transform:uppercase;color:#888}
.section-title{font-size:12px;text-transform:uppercase;color:var(--dark);margin:7px 0 4px;letter-spacing:1px}
.rule{width:40px;height:2px;background:var(--accent);margin:0 auto 10px}
.about p{width:560px;margin:0 auto;font-size:7px;color:var(--muted)}
.link-more{display:inline-block;margin-top:10px;font-size:7px;color:var(--accent);font-weight:700;text-transform:uppercase}

.newsletter{height:160px;position:relative;background:linear-gradient(120deg,#2a241e,#141210 60%,#3a2d20);color:#fff;text-align:center;padding-top:22px}
.newsletter .nl-small{font-size:10px;letter-spacing:1px;text-transform:uppercase;color:#ddd}
.newsletter .nl-big{font-size:22px;letter-spacing:2px;text-transform:uppercase;margin:3px 0 6px}
.newsletter .nl-text{font-size:7px;letter-spacing:.6px;text-transform:uppercase;color:#ccc}
.nl-form{display:flex;justify-content:center;gap:10px;margin-top:16px}
.nl-input{width:150px;height:22px;border:1px solid #888;font-size:6.5px;color:#ccc;text-align:left;padding:6px 8px;text-transform:uppercase}
.nl-btn{background:var(--accent);font-size:7px;font-weight:700;padding:6px 16px;text-transform:uppercase}

.team{height:250px;text-align:center;padding-top:34px}
.members{display:flex;justify-content:space-between;margin-top:8px}
.member{width:130px}
.avatar{width:54px;height:54px;border-radius:50%;margin:0 auto 6px;background:linear-gradient(160deg,#d7dde3,#8b96a1)}
.member-name{font-size:8px;font-weight:700;color:var(--dark)}
.member-text{font-size:6.5px;color:var(--muted);margin:3px 0}
.member-more{font-size:6.5px;color:var(--accent);font-weight:700}

.footer-nav{height:24px;background:var(--dark);display:flex;justify-content:center;align-items:center;gap:16px;font-size:6.5px;color:#ccc;text-transform:uppercase;font-weight:600}
.footer{height:96px;background:var(--darker);color:#aaa;font-size:6.5px;text-align:center;padding-top:12px}
.footer-info{display:flex;justify-content:center;gap:20px}
.footer-info span{display:flex;align-items:center;gap:4px}
.footer-info svg{width:8px;height:8px}
.social{display:flex;justify-content:center;gap:6px;margin:14px 0}
.social span{width:16px;height:16px;border-radius:50%;background:#2f7fbf}
</style>
</head>
<body>
<div class="topbar"><div class="wrap">
  <svg viewBox="0 0 10 10"><path d="M2 1l2 0 1 2.5-1.2 1a6 6 0 0 0 2.7 2.7l1-1.2 2.5 1v2a1 1 0 0 1-1 1A8 8 0 0 1 1 2a1 1 0 0 1 1-1z" fill="#f5a300"/></svg>
  <span>Call Us: 0207 400 1180</span>
</div></div>

<header class="header"><div class="wrap">
  <div class="brand"><span class="brand-mark"></span><span class="brand-name">Brackwell Counsel Partners</span></div>
  <nav class="nav"><span class="active">Home</span><span>About Us</span><span>Join Us</span><span>Contact</span><span>Blog</span><span>Login | Signup</span></nav>
</div></header>

<section class="hero">
  <div class="hero-photo" role="img" aria-label="Lawyer's hand with gavel and documents on a desk"></div>
  <div class="hero-content">
    <div class="hero-kicker serif">Immigration Law</div>
    <h1 class="hero-title serif">Brackwell Counsel Partners</h1>
    <p class="hero-text">We give clear, honest and affordable immigration advice to every client, with regulated advisers who guide each case from start to finish.</p>
    <span class="btn">Read More</span>
  </div>
</section>

<section class="services"><div class="wrap">
  <div class="cards">
    <div class="card">
      <div class="card-title">Consectetur Adipiscing</div>
      <div class="card-photo" role="img" aria-label="Team of advisers in a meeting"></div>
      <p class="card-text">Quis autem vel eum iure reprehenderit qui in ea voluptate velit esse nihil.</p>
      <span class="btn-outline">Know More</span>
    </div>
    <div class="card">
      <div class="card-title">Perspiciatis Unde Omnis</div>
      <div class="card-photo" role="img" aria-label="Business people shaking hands"></div>
      <p class="card-text">Quis autem vel eum iure reprehenderit qui in ea voluptate velit esse nihil.</p>
      <span class="btn-outline">Know More</span>
    </div>
    <div class="card">
      <div class="card-title">Temporibus Autem Quibu</div>
      <div class="card-photo" role="img" aria-label="Adviser consulting with clients at a table"></div>
      <p class="card-text">Quis autem vel eum iure reprehenderit qui in ea voluptate velit esse nihil.</p>
      <span class="btn-outline">Know More</span>
    </div>
  </div>
  <aside class="contact">
    <h3 class="serif">Contact Us</h3>
    <div class="field">Name</div>
    <div class="field">Company name</div>
    <div class="field">Email</div>
    <div class="field tall">Comment</div>
    <span class="submit">Submit</span>
  </aside>
</div></section>

<section class="about">
  <div class="eyebrow">Temporibus autem quibusdam et aut officiis debitis aut rerum</div>
  <h2 class="section-title serif">About Our Firm</h2>
  <div class="rule"></div>
  <p>Brackwell Counsel Partners is regulated to give immigration advice and we have built our name on sound, good value legal work for every client. Most of our clients come to us through personal recommendation, and we are known for our up to date legal knowledge, attention to detail and the care we give to each case from the first meeting onward.</p>
  <span class="link-more">Read More &rarr;</span>
</section>

<section class="newsletter" role="img" aria-label="Dark background with gavel on a desk">
  <div class="nl-small serif">Subscribe for</div>
  <div class="nl-big serif">Newslatter</div>
  <div class="nl-text">Temporibus autem quibusdam et aut officiis debitis aut rerum</div>
  <div class="nl-form"><span class="nl-input">Enter Name</span><span class="nl-input">Enter Email</span><span class="nl-btn">Subscribe</span></div>
</section>

<section class="team"><div class="wrap">
  <div class="eyebrow">Temporibus autem quibusdam et aut officiis debitis aut rerum</div>
  <h2 class="section-title serif">Meet Our Team</h2>
  <div class="rule"></div>
  <div class="members">
    <div class="member"><div class="avatar" role="img" aria-label="Portrait of team member"></div><div class="member-name">Oliver Hayes</div><p class="member-text">Senior adviser who leads visa and settlement cases for families and workers.</p><span class="member-more">Read More</span></div>
    <div class="member"><div class="avatar" role="img" aria-label="Portrait of team member"></div><div class="member-name">Oliver Hayes</div><p class="member-text">Senior adviser who leads visa and settlement cases for families and workers.</p><span class="member-more">Read More</span></div>
    <div class="member"><div class="avatar" role="img" aria-label="Portrait of team member"></div><div class="member-name">Oliver Hayes</div><p class="member-text">Senior adviser who leads visa and settlement cases for families and workers.</p><span class="member-more">Read More</span></div>
    <div class="member"><div class="avatar" role="img" aria-label="Portrait of team member"></div><div class="member-name">Oliver Hayes</div><p class="member-text">Senior adviser who leads visa and settlement cases for families and workers.</p><span class="member-more">Read More</span></div>
  </div>
</div></section>

<nav class="footer-nav"><span>Home</span><span>About Us</span><span>Join Us</span><span>Contact</span><span>Blog</span></nav>
<footer class="footer">
  <div class="footer-info">
    <span><svg viewBox="0 0 10 10"><path d="M2 1l2 0 1 2.5-1.2 1a6 6 0 0 0 2.7 2.7l1-1.2 2.5 1v2a1 1 0 0 1-1 1A8 8 0 0 1 1 2a1 1 0 0 1 1-1z" fill="#f5a300"/></svg>0207 400 1180</span>
    <span><svg viewBox="0 0 10 10"><path d="M5 0.5a3.3 3.3 0 0 0-3.3 3.3C1.7 6.3 5 9.5 5 9.5s3.3-3.2 3.3-5.7A3.3 3.3 0 0 0 5 .5zm0 4.6a1.3 1.3 0 1 1 0-2.6 1.3 1.3 0 0 1 0 2.6z" fill="#f5a300"/></svg>Brackwell Counsel Partners, 14 Marlow Row, London W9 2QT</span>
  </div>
  <div class="social"><span></span><span></span><span></span></div>
  <div>&copy; 2016 BY BRACKWELL COUNSEL PARTNERS</div>
</footer>
</body>
</html>
```